Granite Ridge Response Business Card

Side 1: Granite Ridge Response Logo (logo without Maltese cross) with industrial rope rescue related theme. Our company services - TRAINING - Fire Training, Confined Space Rescue Training, Rope Rescue training, Hazmat Training, Incident Command, EMS, Pump Operations Training. Website - graniteridgeresponse.example.
Side 2: Granite Ridge Response Fire Department Logo (logo with Maltese cross) with Firefighter related theme. Company (division) services - FIELD SERVICES - Fire Department, Stand-by Rescue, Safety, EMS, Planning. "Supporting the Emergency Response Community Since 1967"

Add contact information wherever it makes since (Name, Email, Phone).
I would like it to represent the Granite Ridge Response Fire Department Logo as a division not as a separate entity without saying it, possibly by depicting it in the background of Side 2 instead of being a standalone picture like the logo on Side 1.

```html
<!DOCTYPE html>
<html lang="en">
<head>
<meta charset="utf-8">
<title>Granite Ridge Response Business Card</title>
<link href="https://fonts.googleapis.com/css2?family=Montserrat:wght@500;700;800&family=Lato:wght@400;700&display=swap" rel="stylesheet">
<style>
  :root {
    --page: #2a2b2d;
    --charcoal: #3a3b3e;
    --charcoal-deep: #2e2f31;
    --signal-red: #e0262a;
    --ember: #e2452a;
    --ember-deep: #c9331f;
    --ink: #2f3033;
    --pill: #3d3e41;
    --white: #ffffff;
    --muted: #8a8b8e;
  }
  * { box-sizing: border-box; margin: 0; padding: 0; }
  html, body { width: 1200px; height: 817px; overflow: hidden; }
  body {
    background: var(--page);
    font-family: "Lato", sans-serif;
    position: relative;
  }
  .card {
    position: absolute;
    width: 540px;
    height: 310px;
    border-radius: 22px;
    overflow: hidden;
  }

  /* Side 1 — training */
  .card--training {
    left: 50px; top: 90px;
    background: var(--charcoal);
  }
  .training-photo {
    position: absolute; inset: 0;
    background: radial-gradient(ellipse at 30% 55%, #4a4b4e 0%, var(--charcoal) 55%, var(--charcoal-deep) 100%);
  }
  .rule {
    position: absolute; left: 0; right: 0; height: 2px;
    background: var(--signal-red);
  }
  .rule--top { top: 34px; left: 260px; }
  .rule--bottom { bottom: 34px; }
  .brand {
    position: absolute;
    display: flex; align-items: center; gap: 10px;
  }
  .brand__mark {
    width: 16px; height: 16px;
    background: var(--signal-red);
    flex-shrink: 0;
  }
  .brand__name {
    font-family: "Montserrat", sans-serif;
    font-weight: 800;
    text-transform: uppercase;
    line-height: 1.05;
  }
  .card--training .brand { left: 34px; top: 118px; }
  .card--training .brand__name { color: var(--white); font-size: 22px; letter-spacing: 0.5px; }
  .brand-underline {
    position: absolute; left: 34px; top: 186px;
    width: 210px; height: 2px; background: var(--signal-red);
  }
  .services {
    position: absolute; left: 282px; top: 52px;
    list-style: none;
    color: var(--white);
    font-size: 13px;
    line-height: 20px;
  }
  .services li { position: relative; padding-left: 12px; }
  .services li::before {
    content: ""; position: absolute; left: 0; top: 8px;
    width: 4px; height: 4px; border-radius: 50%;
    background: var(--signal-red);
  }
  .services .services__head { font-weight: 700; letter-spacing: 0.5px; }
  .web-pill {
    position: absolute; left: 150px; bottom: 50px;
    background: var(--signal-red);
    color: var(--white);
    font-size: 12.5px;
    letter-spacing: 2.4px;
    padding: 5px 18px;
    border-radius: 14px;
  }

  /* Side 2 — field services */
  .card--field {
    left: 610px; top: 417px;
    background: var(--white);
  }
  .field-photo {
    position: absolute; left: 0; top: 0; right: 0; height: 212px;
    background: linear-gradient(160deg, #ee6a45 0%, var(--ember) 45%, var(--ember-deep) 100%);
  }
  .card--field .brand {
    left: 0; right: 0; top: 38px;
    justify-content: center;
  }
  .card--field .brand__mark { background: var(--white); }
  .card--field .brand__name { color: var(--white); font-size: 22px; letter-spacing: 1px; }
  .field-rule {
    position: absolute; left: 150px; right: 150px; top: 74px;
    height: 1px; background: rgba(255,255,255,0.8);
  }
  .field-services {
    position: absolute; left: 0; right: 0; top: 98px;
    text-align: center;
    color: var(--white);
    font-family: "Montserrat", sans-serif;
    font-weight: 500;
    font-size: 13px;
    letter-spacing: 0.4px;
    line-height: 21px;
    text-transform: uppercase;
  }
  .motto {
    position: absolute; left: 44px; right: 44px; top: 196px;
    background: var(--pill);
    color: var(--white);
    font-size: 13.5px;
    text-align: center;
    padding: 7px 0;
    border-radius: 18px;
  }
  .person {
    position: absolute; left: 40px; top: 250px;
  }
  .person__name {
    font-family: "Montserrat", sans-serif;
    font-size: 19px;
    font-weight: 500;
    color: var(--ink);
    letter-spacing: 0.6px;
  }
  .person__name strong { color: var(--signal-red); font-weight: 800; }
  .person__role { font-size: 13px; color: var(--muted); margin-top: 1px; }
  .contact {
    position: absolute; left: 300px; top: 248px;
    list-style: none;
    font-size: 11.5px;
    color: var(--ink);
  }
  .contact li { display: flex; align-items: center; gap: 7px; height: 22px; }
  .contact svg { width: 17px; height: 17px; flex-shrink: 0; }
</style>
</head>
<body>

  <section class="card card--training">
    <div class="training-photo" role="img" aria-label="Faint monochrome photo of an industrial rope rescue scene"></div>
    <div class="rule rule--top"></div>
    <div class="brand">
      <span class="brand__mark"></span>
      <span class="brand__name">Granite Ridge<br>Response</span>
    </div>
    <div class="brand-underline"></div>
    <ul class="services">
      <li class="services__head">TRAINING</li>
      <li>Fire Training</li>
      <li>Confined Space Rescue Training</li>
      <li>Rope Rescue training</li>
      <li>Hazmat Training</li>
      <li>Incident Command</li>
      <li>EMS</li>
      <li>Pump Operations Training</li>
    </ul>
    <div class="web-pill">graniteridgeresponse.example</div>
    <div class="rule rule--bottom"></div>
  </section>

  <section class="card card--field">
    <div class="field-photo" role="img" aria-label="Red-toned photo of firefighters walking through smoke at an industrial site"></div>
    <div class="brand">
      <span class="brand__mark"></span>
      <span class="brand__name">Granite Ridge Response</span>
    </div>
    <div class="field-rule"></div>
    <p class="field-services">
      • Field Services • Fire Department • Stand-by Rescue<br>
      • Safety • EMS • Planning
    </p>
    <p class="motto">Supporting the Emergency Response Community Since 1967</p>
    <div class="person">
      <p class="person__name">DANIEL R. <strong>WHITMORE</strong></p>
      <p class="person__role">Managing Director</p>
    </div>
    <ul class="contact">
      <li>
        <svg viewBox="0 0 18 18" aria-hidden="true"><rect width="18" height="18" rx="3" fill="var(--ink)"/><path d="M5.5 4.5l2 0.3 0.8 2.3-1.2 1c0.6 1.3 1.6 2.3 2.9 2.9l1-1.2 2.3 0.8 0.3 2c-0.5 0.6-1.3 0.9-2.1 0.8C8 12.9 5.1 10 4.6 6.6 4.5 5.8 4.9 5 5.5 4.5z" fill="var(--white)"/></svg>
        +00 555 014 22
      </li>
      <li>
        <svg viewBox="0 0 18 18" aria-hidden="true"><rect width="18" height="18" rx="3" fill="var(--ink)"/><rect x="4" y="5.5" width="10" height="7" fill="none" stroke="var(--white)" stroke-width="1.2"/><path d="M4 5.5l5 4 5-4" fill="none" stroke="var(--white)" stroke-width="1.2"/></svg>
        contact@graniteridgeresponse.example
      </li>
    </ul>
  </section>

</body>
</html>
```